Yoga for Scoliosis business card/logo design

I need a business card/logo design for my new business. I am a registered yoga teacher and am certified in yoga for scoliosis. I'd like my card to read "Marlow Yoga Yoga for a Healthy Spine" and would like to incorporate one of the letters in my name{ ie the first vertical line of the letter " H "or "D"} to resemble a scoliotic spine. I regularly teach the following:Yoga for Scoliosis, Yoga for Back Health, Hatha yoga, Vinyasa yoga with Iyengar style alignment. This business is mostly for private clients, but I also teach group, semi-private & work shop classes. I like the colors green (light emerald) and royal blue. I'd like the design to be somewhat sleek, but not too modern. I also like the idea of a ying/yang symbol with a scoliotic spine dviding it.

Danielle Marlow
200 RYT, Certified Yoga for Scoliosis Instructor
MarlowYoga.example
MarlowYoga@mailbox.example
555-412-3097

```html
<!DOCTYPE html>
<html lang="en">
<head>
<meta charset="utf-8">
<title>Marlow Yoga – Business Card</title>
<link rel="stylesheet" href="https://fonts.googleapis.com/css2?family=Open+Sans:wght@300;400;600;700&display=swap">
<style>
  :root {
    --backdrop: #d9d9dc;
    --card-white: #ffffff;
    --royal-blue: #1466c0;
    --royal-blue-light: #2f9ee0;
    --emerald: #5aac1e;
    --emerald-light: #86c232;
    --on-color: #ffffff;
    --on-color-soft: rgba(255,255,255,0.85);
  }
  html, body {
    margin: 0;
    padding: 0;
    width: 1200px;
    height: 960px;
    overflow: hidden;
    background: var(--backdrop);
    font-family: "Open Sans", Arial, sans-serif;
  }
  .business-card {
    position: absolute;
    left: 100px;
    top: 160px;
    width: 1000px;
    height: 640px;
    border-radius: 36px;
    background: var(--card-white);
    overflow: hidden;
    box-shadow: 0 10px 30px rgba(0,0,0,0.18);
  }
  .card-shapes {
    position: absolute;
    inset: 0;
  }
  .credential {
    position: absolute;
    right: 70px;
    top: 56px;
    text-align: right;
    color: var(--on-color);
    font-weight: 300;
    font-size: 34px;
    line-height: 1.3;
  }
  .credential strong {
    font-weight: 600;
  }
  .contact-block {
    position: absolute;
    left: 90px;
    top: 250px;
    width: 440px;
    text-align: center;
    color: var(--on-color);
  }
  .contact-name {
    margin: 0;
    font-weight: 700;
    font-size: 36px;
    letter-spacing: 0.5px;
  }
  .contact-rule {
    height: 2px;
    background: var(--on-color-soft);
    margin: 14px 20px 18px;
  }
  .contact-line {
    margin: 0;
    font-weight: 300;
    font-size: 20px;
    line-height: 1.55;
    color: var(--on-color-soft);
  }
  .brand-name {
    position: absolute;
    right: 40px;
    bottom: 60px;
    width: 250px;
    margin: 0;
    text-align: right;
    font-weight: 400;
    font-size: 22px;
    line-height: 1.4;
    color: var(--royal-blue);
  }
</style>
</head>
<body>
  <div class="business-card">
    <svg class="card-shapes" width="1000" height="640" viewBox="0 0 1000 640" aria-hidden="true">
      <defs>
        <linearGradient id="blue-panel" x1="0" y1="0" x2="1" y2="1">
          <stop offset="0" stop-color="var(--royal-blue-light)"/>
          <stop offset="1" stop-color="var(--royal-blue)"/>
        </linearGradient>
        <linearGradient id="green-panel" x1="0" y1="0" x2="1" y2="1">
          <stop offset="0" stop-color="var(--emerald-light)"/>
          <stop offset="1" stop-color="var(--emerald)"/>
        </linearGradient>
      </defs>
      <path class="blue-panel" fill="url(#blue-panel)"
            d="M470,0 H1000 V110 C880,200 770,330 690,470 L412,124 C440,80 460,40 470,0 Z"/>
      <path class="green-panel" fill="url(#green-panel)"
            d="M0,220 C150,200 280,160 392,136 L674,486 C620,530 580,590 560,640 H0 Z"/>
    </svg>

    <div class="credential">Certified Yoga for<br><strong>Scoliosis</strong> Instructor</div>

    <div class="contact-block">
      <h1 class="contact-name">Danielle Marlow</h1>
      <div class="contact-rule"></div>
      <p class="contact-line">Danielle Marlow 200 RYT</p>
      <p class="contact-line">• MarlowYoga.example • Phone: 555-412-3097</p>
      <p class="contact-line">MarlowYoga@mailbox.example</p>
    </div>

    <p class="brand-name">Marlow Yoga Yoga for a Healthy Spine</p>
  </div>
</body>
</html>
```